flat authentication

design an authentication plate and an authentication certificate

on both you need the Brolo vintage store logo
authentication plate size 10 * 7cm
color black transparent text
aluminum plate material
American vintage spirit in the years 1950 to 1960

an authentication certificate
page size 4
the text to put above is in the word file
color black white red blue golden
on the certificate I would like the round golden pastille (like a seal)

```html
<!DOCTYPE html>
<html lang="en">
<head>
<meta charset="utf-8">
<title>Authentication Plate</title>
<link href="https://fonts.googleapis.com/css2?family=Outfit:wght@500;600;700&display=swap" rel="stylesheet">
<style>
  :root {
    --page: #ffffff;
    --plate-black: #141414;
    --aluminum-cream: #ebe8dc;
    --hole: #ffffff;
  }
  html, body {
    margin: 0;
    padding: 0;
    width: 1200px;
    height: 1000px;
    overflow: hidden;
    background: var(--page);
  }
  .canvas {
    position: relative;
    width: 1200px;
    height: 1000px;
    font-family: "Outfit", sans-serif;
    color: var(--aluminum-cream);
  }
  .plate-shapes {
    position: absolute;
    left: 0;
    top: 0;
  }
  .text {
    position: absolute;
    left: 0;
    width: 1200px;
    text-align: center;
    margin: 0;
    font-weight: 600;
    letter-spacing: 0.5px;
    line-height: 1;
  }
  .brand-name {
    position: absolute;
    left: 468px;
    top: 250px;
    width: 274px;
    height: 112px;
    display: flex;
    align-items: center;
    justify-content: center;
    font-size: 50px;
    font-weight: 700;
    color: var(--plate-black);
    letter-spacing: 1px;
  }
  .origin-label { top: 377px; font-size: 15px; }
  .origin-value { top: 401px; font-size: 21px; }
  .field-label {
    position: absolute;
    top: 442px;
    width: 219px;
    text-align: center;
    font-size: 15px;
    font-weight: 600;
  }
  .field-value {
    position: absolute;
    top: 464px;
    width: 219px;
    height: 51px;
    display: flex;
    align-items: center;
    justify-content: center;
    font-size: 20px;
    font-weight: 700;
    color: var(--plate-black);
    letter-spacing: 1px;
  }
  .col-restoration { left: 262px; }
  .col-model { left: 490px; }
  .col-year { left: 718px; }
  .restoration-note { top: 550px; font-size: 17px; letter-spacing: 0.8px; }
  .store-mark {
    position: absolute;
    left: 470px;
    top: 620px;
    width: 260px;
    display: flex;
    align-items: center;
    justify-content: center;
    gap: 12px;
    font-size: 22px;
    font-weight: 600;
    color: var(--aluminum-cream);
  }
  .store-mark-dot {
    width: 18px;
    height: 18px;
    border-radius: 50%;
    background: var(--aluminum-cream);
  }
</style>
</head>
<body>
<div class="canvas">
  <svg class="plate-shapes" width="1200" height="1000" viewBox="0 0 1200 1000" aria-hidden="true">
    <rect class="plate-rim" x="222" y="213" width="753" height="532" rx="30" fill="var(--aluminum-cream)"/>
    <rect class="plate-face" x="232" y="223" width="733" height="512" rx="22" fill="var(--plate-black)"/>
    <path class="plate-frame" fill="none" stroke="var(--aluminum-cream)" stroke-width="3"
      d="M274 234 L921 234 A30 30 0 0 0 951 264 L951 692 A30 30 0 0 0 921 722 L274 722 A30 30 0 0 0 244 692 L244 264 A30 30 0 0 0 274 234 Z"/>
    <line class="plate-divider" x1="244" y1="534" x2="951" y2="534" stroke="var(--aluminum-cream)" stroke-width="3"/>
    <rect class="brand-badge" x="468" y="250" width="274" height="112" rx="24" fill="var(--aluminum-cream)"/>
    <rect x="262" y="464" width="219" height="51" fill="var(--aluminum-cream)"/>
    <rect x="490" y="464" width="219" height="51" fill="var(--aluminum-cream)"/>
    <rect x="718" y="464" width="219" height="51" fill="var(--aluminum-cream)"/>
    <circle class="mount-hole" cx="258" cy="246" r="7" fill="var(--hole)"/>
    <circle class="mount-hole" cx="938" cy="246" r="7" fill="var(--hole)"/>
    <circle class="mount-hole" cx="258" cy="708" r="7" fill="var(--hole)"/>
    <circle class="mount-hole" cx="938" cy="708" r="7" fill="var(--hole)"/>
  </svg>

  <div class="brand-name">Harlow</div>

  <p class="text origin-label">ORIGIN OF THE PRODUCT</p>
  <p class="text origin-value">MADE IN USA</p>

  <div class="field-label col-restoration">RESTORATION NUMBER</div>
  <div class="field-label col-model">MODEL</div>
  <div class="field-label col-year">YEAR</div>

  <div class="field-value col-restoration">001</div>
  <div class="field-value col-model">910</div>
  <div class="field-value col-year">2021</div>

  <p class="text restoration-note">RESTORATION IN BELGIUM BY OUR CRAFTMAN</p>

  <div class="store-mark">
    <span class="store-mark-dot"></span>
    <span>Brolo vintage store</span>
  </div>
</div>
</body>
</html>
```